Business Cards for IT Consulting Company (Managed Service Provider)

I am looking to have some business cards printed and would like some designs. We are an IT Consulting company based in Vancouver BC. I would like a nice clean and modern look to the cards. I have uploaded all the versions of my logo so parts can be used as needed. Here is a snippit from our website homepage:

Kelbrook Systems Ltd. is an IT Solutions Partner located in Vancouver BC, Canada. We offer IT solutions and support to customers in the greater Vancouver Area. With expertise in Microsoft platforms, as well as Linux and Mac OSX and over 12 years experience in the IT industry, Kelbrook Systems is dedicated to offering our clients top quality service and products. We take pride in the solutions we offer our customers. The greatest compliment a client can give us is to recommend our services.

Kelbrook Systems Ltd. offers a wide range of IT services from onsite service to remote support and managed service solutions. This allows clients to choose the support path that best suits their company’s needs. Supporting many different sized companies from small to enterprise level over the past 12 years Kelbrook Systems has the experience and expertise needed to ensure things run smoothly. Allowing our clients to focus on doing business.

Building Dependable Technology For Growing Teams.

Kelbrook Systems is dedicated to providing our clients with IT solutions that work and grow with them for years to come. This philosophy helps save money in the long run instead of replacing equipment constantly. Far too often IT solutions are not well thought out and while possibly solving the problem at hand, require replacement due to growth or quality within a very short time frame. Kelbrook Systems takes pride in providing solutions that will last and be able to accommodate growth without the need for replacement.

Industry/Entity Type

Information Technology

Contact Information for Business Card

Kelbrook Systems Ltd.
(Employee Name)
Eml: (Employees Email Address)
Web: kelbrook.me
Ph: 604-555-0142

Font styles to use
Serif
Sans Serif

Requirements
Must have
• The Company logo and company colors.
Nice to have
• - Our tag line: "Revolutionizing IT Services" or "Building Dependable Technology For Growing Teams."
• - Also I really like the idea of nature and technology together blending which is sort of where my logo came from so integrating that somehow onto the business cards would be great.

```html
<!DOCTYPE html>
<html lang="en">
<head>
<meta charset="utf-8">
<title>Kelbrook Systems Ltd. – Business Cards</title>
<link href="https://fonts.googleapis.com/css2?family=Open+Sans:wght@400;600;700&display=swap" rel="stylesheet">
<style>
  :root {
    --bg: #ecebe8;
    --card: #ffffff;
    --brand-blue: #27a9e1;
    --text-grey: #5b5b5b;
    --soft-grey: #8a8a8a;
    --pattern-light: #f4f4f4;
    --pattern-mid: #e4e4e4;
    --shadow: rgba(0, 0, 0, 0.18);
  }
  * { box-sizing: border-box; margin: 0; padding: 0; }
  html, body {
    width: 1200px; height: 1023px; overflow: hidden;
    background: var(--bg);
    font-family: "Open Sans", Arial, sans-serif;
  }
  .canvas { position: relative; width: 1200px; height: 1023px; }

  .card {
    position: absolute;
    width: 620px; height: 354px;
    background: var(--card);
    box-shadow: 0 10px 28px var(--shadow);
  }
  .card--front { left: 70px; top: 100px; }
  .card--back  { left: 510px; top: 560px; overflow: hidden; }

  /* Front */
  .wordmark {
    position: absolute; left: 52px; top: 70px;
    display: flex; align-items: center; gap: 14px;
  }
  .wordmark__square {
    width: 34px; height: 34px; background: var(--brand-blue);
  }
  .wordmark__name {
    font-size: 30px; font-weight: 700; color: var(--brand-blue);
    letter-spacing: -0.2px;
  }
  .person { position: absolute; left: 190px; top: 160px; }
  .person__name { font-size: 24px; font-weight: 600; color: var(--text-grey); }
  .person__first { color: var(--brand-blue); }
  .person__role { font-size: 13px; color: var(--soft-grey); margin-top: 2px; }

  .contact { position: absolute; left: 190px; top: 236px; list-style: none; }
  .contact__item {
    display: flex; align-items: center; gap: 9px;
    font-size: 15px; color: var(--text-grey); line-height: 27px;
  }
  .contact__icon { width: 13px; height: 13px; flex: none; }

  /* Back */
  .back-pattern {
    position: absolute; inset: 0;
    background: linear-gradient(135deg, var(--pattern-light), var(--pattern-mid) 50%, var(--pattern-light));
  }
  .back-mark {
    position: absolute; left: 0; right: 0; top: 140px;
    display: flex; justify-content: center; align-items: center; gap: 14px;
  }
  .back-mark__square { width: 30px; height: 30px; background: var(--brand-blue); }
  .back-mark__name { font-size: 28px; font-weight: 700; color: var(--brand-blue); }
  .tagline {
    position: absolute; left: 28px; bottom: 22px;
    font-size: 14px; letter-spacing: 1px; color: var(--text-grey);
  }
</style>
</head>
<body>
<main class="canvas">

  <section class="card card--front" aria-label="Business card front">
    <div class="wordmark">
      <span class="wordmark__square"></span>
      <span class="wordmark__name">Kelbrook Systems Ltd.</span>
    </div>

    <div class="person">
      <p class="person__name"><span class="person__first">Dana</span> Marsh</p>
      <p class="person__role">Director</p>
    </div>

    <ul class="contact">
      <li class="contact__item">
        <svg class="contact__icon" viewBox="0 0 16 16"><circle cx="8" cy="8" r="8" fill="#27a9e1"/><path d="M5 4.5l1.6-.4.8 2-1 .8a6 6 0 0 0 2.7 2.7l.8-1 2 .8-.4 1.6C9 11.5 4.5 7 5 4.5z" fill="#fff"/></svg>
        604-555-0142
      </li>
      <li class="contact__item">
        <svg class="contact__icon" viewBox="0 0 16 16"><rect x="0" y="3" width="16" height="11" rx="1" fill="#27a9e1"/><path d="M1 4l7 5 7-5" stroke="#fff" stroke-width="1.3" fill="none"/></svg>
        Employees@kelbrooksystems.com
      </li>
      <li class="contact__item">
        <svg class="contact__icon" viewBox="0 0 16 16"><circle cx="8" cy="8" r="7.5" fill="#27a9e1"/><g stroke="#fff" stroke-width="1" fill="none"><ellipse cx="8" cy="8" rx="3" ry="7"/><path d="M1 8h14M2 4.5h12M2 11.5h12"/></g></svg>
        www.kelbrooksystems.com
      </li>
    </ul>
  </section>

  <section class="card card--back" aria-label="Business card back">
    <div class="back-pattern" role="img" aria-label="Light grey repeating hexagon pattern background"></div>
    <div class="back-mark">
      <span class="back-mark__square"></span>
      <span class="back-mark__name">Kelbrook Systems</span>
    </div>
    <p class="tagline">Building Dependable Technology For Growing Teams.</p>
  </section>

</main>
</body>
</html>
```